professional looking data specialist website

I've recently had a new logo designed and I'm now looking to get a professional looking website built. This is for a new company that specialises in data. We look to support companies with business intelligence, report modelling, data governance to new european legislation (GDPR). We are offer consultancy or we can attend site and complete work when required. Our target arket is united kingdom wide and we are specifically aiming at small to medium sized companies.

Target Market(s)

small to medium enterprise companies from all industries

Industry/Entity Type

Professional Service

Coding

Coded - Design and coding required

Number of Pages Required

4 page

Font styles to use
Sans Serif

Colors

Designer to choose colors to be used in the design.

Requirements
Must have
• Professional look including the company logo, need to have ability to request more information from us so needs a inquiries page, seperate pages for the different offerings, data governance, report modelling, business intelligence implementation, data protection
Nice to have
• any website interaction, animation, etc
Should not have
• too many colours, too busy pages, must look professional

```html
<!DOCTYPE html>
<html lang="en">
<head>
<meta charset="utf-8">
<title>Harbourline Data</title>
<link rel="stylesheet" href="https://fonts.googleapis.com/css2?family=Roboto:wght@300;400;500;700&display=swap">
<style>
:root{
  --navy:#122b4f;
  --navy-deep:#0c1f3b;
  --blue:#1f6fb8;
  --blue-light:#3d8ad6;
  --ink:#2b2f36;
  --muted:#7a8290;
  --line:#e1e4e9;
  --paper:#ffffff;
  --soft:#f1f3f6;
}
*{box-sizing:border-box;margin:0;padding:0}
html,body{width:1200px;height:5199px;overflow:hidden}
body{font-family:"Roboto",Arial,sans-serif;color:var(--ink);background:var(--paper);position:relative}
.section{position:absolute;left:0;width:1200px}
.eyebrow{font-size:13px;letter-spacing:2px;color:var(--muted);text-transform:uppercase;text-align:center}
.heading{font-size:30px;font-weight:400;text-align:center;color:var(--ink);margin-top:8px}
.btn{display:inline-block;font-size:15px;padding:13px 24px;border-radius:3px;color:#fff;text-decoration:none}
.btn-solid{background:var(--blue)}
.btn-outline{border:1px solid rgba(255,255,255,.8)}
.arrows{position:absolute;left:0;width:1200px;text-align:center}
.arrow{display:inline-block;width:44px;height:44px;border-radius:50%;background:var(--blue);margin:0 6px;position:relative}
.arrow svg{position:absolute;left:14px;top:14px}

/* header */
.site-header{top:0;height:90px;background:var(--paper);box-shadow:0 1px 4px rgba(0,0,0,.15);z-index:3}
.brand{position:absolute;left:40px;top:18px;display:flex;align-items:center;gap:10px}
.brand-mark{width:44px;height:44px;background:var(--blue)}
.brand-name{font-size:30px;font-weight:500;color:var(--navy)}
.main-nav{position:absolute;right:190px;top:0;display:flex;height:90px;align-items:center}
.main-nav a{font-size:15px;color:var(--ink);text-decoration:none;padding:0 18px;line-height:90px;border-right:1px solid var(--line)}
.main-nav a.current{color:var(--blue);border-bottom:3px solid var(--blue)}
.social{position:absolute;right:40px;top:30px;display:flex;gap:8px}
.social span{width:30px;height:30px;border:1px solid var(--line);display:block}

/* hero */
.hero{top:90px;height:798px;background:linear-gradient(100deg,#0f2747 0%,#1b3d6b 55%,#34598b 100%)}
.hero-photo{position:absolute;right:0;top:0;width:640px;height:798px;background:radial-gradient(ellipse at 60% 45%,#6f8fb8 0%,#2e5183 50%,rgba(27,61,107,0) 80%)}
.hero-text{position:absolute;left:48px;top:210px;color:#fff}
.hero-text h1{font-size:52px;font-weight:400;line-height:1.15}
.hero-text .tag{font-size:15px;margin-top:14px;opacity:.85}
.hero-text ul{list-style:none;margin-top:26px}
.hero-text li{font-size:16px;line-height:30px;padding-left:18px;position:relative}
.hero-text li:before{content:"";position:absolute;left:0;top:13px;width:6px;height:6px;background:#fff;border-radius:50%}
.hero-actions{margin-top:36px;display:flex;gap:14px}

/* services */
.services{top:888px;height:412px}
.services .eyebrow{margin-top:40px}
.service-grid{position:absolute;left:43px;top:120px;display:flex;gap:24px}
.service-card{width:259px;height:250px;border:1px solid var(--line);text-align:center;padding-top:36px;box-shadow:0 2px 6px rgba(0,0,0,.06)}
.service-icon{width:56px;height:56px;background:var(--blue);margin:0 auto;display:flex;align-items:center;justify-content:center}
.service-card h3{font-size:16px;font-weight:500;color:var(--navy);margin-top:24px;text-transform:uppercase;line-height:1.3}
.service-card p{font-size:14px;color:var(--muted);margin:12px 24px 0;line-height:1.5}

/* projects */
.projects{top:1300px;height:468px;background:var(--soft)}
.projects .eyebrow{margin-top:30px}
.project-grid{position:absolute;left:43px;top:95px;display:flex;gap:22px}
.project-card{width:260px;background:var(--paper)}
.project-photo{height:160px}
.project-card h4{font-size:16px;font-weight:400;padding:14px 16px 6px;line-height:1.35}
.project-card p{font-size:13px;color:var(--muted);padding:0 16px 16px;line-height:1.5}

/* growth */
.growth{top:1768px;height:399px;background:linear-gradient(90deg,#163766 0%,#1d4a82 100%)}
.growth-text{position:absolute;left:48px;top:110px;width:430px;color:#fff}
.growth-text h2{font-size:30px;font-weight:400}
.growth-text p{font-size:14px;opacity:.8;margin:16px 0 28px;line-height:1.55}
.growth-chart{position:absolute;left:560px;top:30px}

/* testimonials */
.testimonials{top:2167px;height:485px}
.testimonials .eyebrow{margin-top:40px}
.quote-grid{position:absolute;left:43px;top:115px;display:flex;gap:22px}
.quote{width:260px}
.quote-box{border:1px solid var(--line);padding:22px;height:268px;font-size:14px;line-height:1.6;color:var(--ink)}
.person{display:flex;gap:12px;margin-top:22px;align-items:center}
.avatar{width:48px;height:48px;border-radius:50%;background:#9aa7b8}
.person b{display:block;font-size:14px;font-weight:500}
.person span{font-size:13px;color:var(--muted)}

/* news */
.news{top:2652px;height:814px;background:linear-gradient(180deg,#c9a9a8 0%,#c4b6bf 30%,#aab3c2 60%,#8c97a8 100%)}
.news-head{position:absolute;top:20px;width:1200px;text-align:center}
.news-head .eyebrow{color:#3c4350}
.news-head p{font-size:14px;color:#2f3540;margin-top:8px;line-height:1.5}
.news-grid{position:absolute;left:43px;top:200px;display:flex;gap:24px}
.news-card{width:354px;background:var(--paper)}
.news-photo{height:215px}
.news-card h4{font-size:20px;font-weight:400;padding:20px 22px 10px;line-height:1.3;height:110px}
.news-meta{border-top:1px solid var(--line);font-size:12px;color:var(--muted);padding:12px 22px;letter-spacing:.5px}

/* clients */
.clients{top:3466px;height:629px}
.clients .eyebrow{margin-top:40px}
.clients .intro{text-align:center;font-size:14px;color:var(--muted);margin-top:14px;line-height:1.5}
.client-grid{position:absolute;left:100px;top:230px;width:1000px;display:grid;grid-template-columns:repeat(4,1fr);row-gap:120px}
.client-badge{width:130px;height:50px;margin:0 auto;background:#c4c9d1;border-radius:4px}

/* call to action */
.cta{top:4095px;height:303px;background:linear-gradient(90deg,#15335e,#1c4478);text-align:center;color:#fff}
.cta h2{font-size:42px;font-weight:400;margin-top:85px}
.cta p{font-size:14px;opacity:.8;margin:12px 0 26px}

/* footer */
.site-footer{top:4398px;height:758px;background:var(--paper)}
.footer-brand{position:absolute;left:43px;top:70px;width:250px}
.footer-brand .brand-mark{width:56px;height:56px;background:var(--blue);margin-bottom:12px}
.footer-brand .brand-name{font-size:30px}
.footer-brand p{font-size:14px;color:var(--muted);margin-top:10px;line-height:1.5}
.footer-col{position:absolute;top:70px;width:250px}
.footer-col h5{font-size:14px;letter-spacing:1.5px;text-transform:uppercase;font-weight:500;margin-bottom:18px}
.footer-col li{list-style:none;font-size:14px;color:var(--muted);line-height:34px;border-bottom:1px solid var(--line)}
.contact li{border:none;padding-left:22px;position:relative}
.contact li span{position:absolute;left:0;top:11px;width:11px;height:11px;background:var(--blue);border-radius:2px}
.copyright{top:5156px;height:43px;background:var(--soft);font-size:12px;color:var(--muted);text-align:center;line-height:43px}
</style>
</head>
<body>

<header class="section site-header">
  <div class="brand"><div class="brand-mark"></div><span class="brand-name">Harbourline Data</span></div>
  <nav class="main-nav">
    <a class="current">Home</a><a>About Us</a><a>Our Services</a><a>Success Stories</a><a>Privacy Blog</a><a>Contact Us</a>
  </nav>
  <div class="social"><span></span><span></span><span></span></div>
</header>

<section class="section hero">
  <div class="hero-photo" role="img" aria-label="Business person touching a phone screen showing the company name and data charts"></div>
  <div class="hero-text">
    <h1>We know your future<br>customers...</h1>
    <p class="tag">...and when they are ready to buy.</p>
    <ul>
      <li>Business Intelligence Implementation</li>
      <li>Report modelling</li>
      <li>Data governance (GDPR)</li>
      <li>Data protection</li>
    </ul>
    <div class="hero-actions"><a class="btn btn-solid">Read More</a><a class="btn btn-outline">About Us</a></div>
  </div>
</section>

<section class="section services">
  <p class="eyebrow">Our Services</p>
  <h2 class="heading">We help technology companies grow quickly.</h2>
  <div class="service-grid">
    <div class="service-card">
      <div class="service-icon"><svg width="26" height="26" viewBox="0 0 26 26"><path d="M13 2 L23 6 V13 C23 19 18 23 13 24 C8 23 3 19 3 13 V6 Z" fill="#fff"/></svg></div>
      <h3>Data Governance</h3>
      <p>Lorem ipsum dolor sit amet, conse adipiscing elit. Prae eget travestie vitae.</p>
    </div>
    <div class="service-card">
      <div class="service-icon"><svg width="26" height="26" viewBox="0 0 26 26"><rect x="3" y="14" width="5" height="9" fill="#fff"/><rect x="10.5" y="8" width="5" height="15" fill="#fff"/><rect x="18" y="3" width="5" height="20" fill="#fff"/></svg></div>
      <h3>Report Modelling</h3>
      <p>Lorem ipsum dolor sit amet, conse adipiscing elit. Prae eget travestie vitae.</p>
    </div>
    <div class="service-card">
      <div class="service-icon"><svg width="26" height="26" viewBox="0 0 26 26"><circle cx="13" cy="11" r="8" fill="#fff"/><rect x="9" y="19" width="8" height="5" fill="#fff"/></svg></div>
      <h3>Business Intelligence<br>Implementation</h3>
      <p>Lorem ipsum dolor sit amet, conse adipiscing elit. Prae eget travestie vitae.</p>
    </div>
    <div class="service-card">
      <div class="service-icon"><svg width="26" height="26" viewBox="0 0 26 26"><rect x="4" y="11" width="18" height="13" fill="#fff"/><path d="M8 11 V8 A5 5 0 0 1 18 8 V11" stroke="#fff" stroke-width="2.5" fill="none"/></svg></div>
      <h3>Data Protection</h3>
      <p>Lorem ipsum dolor sit amet, conse adipiscing elit. Prae eget travestie vitae.</p>
    </div>
  </div>
</section>

<section class="section projects">
  <p class="eyebrow">Showcase</p>
  <h2 class="heading">Our Latest Projects</h2>
  <div class="project-grid">
    <div class="project-card"><div class="project-photo" role="img" aria-label="Team meeting around a table" style="background:linear-gradient(135deg,#8d7a6c,#c3b3a2)"></div><h4>Pellentesque elit risus conse adipiscing</h4><p>Lorem ipsum dolor sit amet, conse adipiscing elit. Prae eget travestie vitae.</p></div>
    <div class="project-card"><div class="project-photo" role="img" aria-label="Colleagues working together at a desk" style="background:linear-gradient(135deg,#b68a5c,#e0c39c)"></div><h4>Aliquam sodales quam quis port eget</h4><p>Lorem ipsum dolor sit amet, conse adipiscing elit. Prae eget travestie vitae.</p></div>
    <div class="project-card"><div class="project-photo" role="img" aria-label="Group presentation in a bright office" style="background:linear-gradient(135deg,#a7b0b8,#dfe3e6)"></div><h4>Mauris facili dapibus dolor sit amet</h4><p>Lorem ipsum dolor sit amet, conse adipiscing elit. Prae eget travestie vitae.</p></div>
    <div class="project-card"><div class="project-photo" role="img" aria-label="Hands over reports and charts on a table" style="background:linear-gradient(135deg,#7d93aa,#c9d3dd)"></div><h4>Lorem ipsum dolor sit amet conse</h4><p>Lorem ipsum dolor sit amet, conse adipiscing elit. Prae eget travestie vitae.</p></div>
  </div>
  <div class="arrows" style="top:400px">
    <span class="arrow"><svg width="16" height="16" viewBox="0 0 16 16"><path d="M10 3 L5 8 L10 13" stroke="#fff" stroke-width="2" fill="none"/></svg></span>
    <span class="arrow"><svg width="16" height="16" viewBox="0 0 16 16"><path d="M6 3 L11 8 L6 13" stroke="#fff" stroke-width="2" fill="none"/></svg></span>
  </div>
</section>

<section class="section growth">
  <div class="growth-text">
    <h2>We Help You Grow</h2>
    <p>Lorem ipsum dolor sit amet, conse adipiscing elit. Maecenas mauris leo, pellentesque at vestibulum quis, porttitor eget turpis. Morbi porta arcu vel semper pulvinar. Aenean in velit quis risus ultricies pretium. Etiam in sapien et mi.</p>
    <a class="btn btn-solid">Our Portfolio</a>
  </div>
  <svg class="growth-chart" width="600" height="340" viewBox="0 0 600 340" aria-label="Line chart of rising growth">
    <g stroke="rgba(255,255,255,.35)" stroke-width="1">
      <line x1="60" y1="20" x2="590" y2="20"/><line x1="60" y1="60" x2="590" y2="60"/><line x1="60" y1="100" x2="590" y2="100"/><line x1="60" y1="140" x2="590" y2="140"/><line x1="60" y1="180" x2="590" y2="180"/><line x1="60" y1="220" x2="590" y2="220"/><line x1="60" y1="260" x2="590" y2="260"/><line x1="60" y1="300" x2="590" y2="300"/>
      <line x1="60" y1="20" x2="60" y2="300"/><line x1="148" y1="20" x2="148" y2="300"/><line x1="236" y1="20" x2="236" y2="300"/><line x1="324" y1="20" x2="324" y2="300"/><line x1="412" y1="20" x2="412" y2="300"/><line x1="500" y1="20" x2="500" y2="300"/><line x1="590" y1="20" x2="590" y2="300"/>
    </g>
    <g fill="rgba(255,255,255,.7)" font-size="10" font-family="Roboto,Arial,sans-serif">
      <text x="10" y="24">70000</text><text x="10" y="64">60000</text><text x="10" y="104">50000</text><text x="10" y="144">40000</text><text x="10" y="184">30000</text><text x="10" y="224">20000</text><text x="10" y="264">10000</text><text x="28" y="304">0</text>
      <text x="48" y="322">2011</text><text x="136" y="322">2012</text><text x="224" y="322">2013</text><text x="312" y="322">2014</text><text x="400" y="322">2015</text><text x="488" y="322">2016</text><text x="570" y="322">2017</text>
    </g>
    <polyline points="80,285 120,270 160,230 200,205 240,175 280,160 320,150 360,140 400,128 440,118 480,112 520,96 560,70 585,40" fill="none" stroke="#fff" stroke-width="2" stroke-dasharray="5 3"/>
    <g fill="#fff"><circle cx="80" cy="285" r="3"/><circle cx="160" cy="230" r="3"/><circle cx="240" cy="175" r="3"/><circle cx="320" cy="150" r="3"/><circle cx="400" cy="128" r="3"/><circle cx="480" cy="112" r="3"/><circle cx="560" cy="70" r="3"/><circle cx="585" cy="40" r="3"/></g>
  </svg>
</section>

<section class="section testimonials">
  <p class="eyebrow">Check Our</p>
  <h2 class="heading">Testimonials</h2>
  <div class="quote-grid">
    <div class="quote"><div class="quote-box">Lorem ipsum dolor sit amet, conse adipiscing elit. Maecenas mauris leo, pellentesque at vestibulum quis, porttitor eget turpis. Morbi porta arcu vel semper pulvinar.</div><div class="person"><div class="avatar"></div><div><b>Daniel Ashworth</b><span>CEO, Manager</span></div></div></div>
    <div class="quote"><div class="quote-box">Sed hendrerit quam sed ante euismod pellentesque. Etiam in ullamcorper nisi. Proin ante arcu, aliquam vel nisi eget, convallis sagittis justo. Mauris mollis magna sapien.</div><div class="person"><div class="avatar"></div><div><b>Priya Lomax</b><span>CEO, Director</span></div></div></div>
    <div class="quote"><div class="quote-box">Vivamus id ex non quam aliquet lobortis et ullamcorper nisl. Nunc vel neque a lacus dictum venenatis. Proin ante arcu, aliquam vel nisi eget, consequat vitae.</div><div class="person"><div class="avatar"></div><div><b>Tom Everard</b><span>President, Allied</span></div></div></div>
    <div class="quote"><div class="quote-box">Sed hendrerit quam sed ante euismod tellus. Etiam in ullamcorper nisi. Proin ante arcu, aliquam vel nisi eget, convallis sagittis justo nulla.</div><div class="person"><div class="avatar"></div><div><b>Clara Whitby</b><span>CEO, Partner</span></div></div></div>
  </div>
</section>

<section class="section news" role="img" aria-label="City skyline with clock tower at dusk behind the news cards">
  <div class="news-head">
    <p class="eyebrow">See Our</p>
    <h2 class="heading">Latest News</h2>
    <p>Harbourline Data provides you daily fresh news related to our works and achievements.<br>Be ready to keep in touch with us and stay tuned!</p>
  </div>
  <div class="news-grid">
    <div class="news-card"><div class="news-photo" role="img" aria-label="Hands using a laptop" style="background:linear-gradient(135deg,#9aa7b5,#d6dde4)"></div><h4>Diam eu sapien et purus ultricies tempor nabh</h4><div class="news-meta">18 JANUARY &nbsp;·&nbsp; READ MORE</div></div>
    <div class="news-card"><div class="news-photo" role="img" aria-label="Business people standing in conversation" style="background:linear-gradient(135deg,#6d7682,#c9cfd6)"></div><h4>Phasellus eget augue est fring</h4><div class="news-meta">18 JANUARY &nbsp;·&nbsp; READ MORE</div></div>
    <div class="news-card"><div class="news-photo" role="img" aria-label="Two colleagues reviewing work at a desk" style="background:linear-gradient(135deg,#b19a84,#e2d6c8)"></div><h4>Usque ac gravida ligula nunc nec mus</h4><div class="news-meta">18 JANUARY &nbsp;·&nbsp; READ MORE</div></div>
  </div>
  <div class="arrows" style="top:630px">
    <span class="arrow"><svg width="16" height="16" viewBox="0 0 16 16"><path d="M10 3 L5 8 L10 13" stroke="#fff" stroke-width="2" fill="none"/></svg></span>
    <span class="arrow"><svg width="16" height="16" viewBox="0 0 16 16"><path d="M6 3 L11 8 L6 13" stroke="#fff" stroke-width="2" fill="none"/></svg></span>
  </div>
</section>

<section class="section clients">
  <p class="eyebrow">See Why</p>
  <h2 class="heading">Clients Trust Us</h2>
  <p class="intro">We cooperate with businesses and international companies all over the world.<br>Some of our partners and customers are listed below.</p>
  <div class="client-grid">
    <div class="client-badge"></div><div class="client-badge"></div><div class="client-badge"></div><div class="client-badge"></div>
    <div class="client-badge"></div><div class="client-badge"></div><div class="client-badge"></div><div class="client-badge"></div>
  </div>
</section>

<section class="section cta">
  <h2>What can we do for you?</h2>
  <p>Drop us an email and we'll get back to you as soon as we can.</p>
  <a class="btn btn-outline">Contact Us</a>
</section>

<footer class="section site-footer">
  <div class="footer-brand">
    <div class="brand-mark"></div>
    <span class="brand-name">Harbourline Data</span>
    <p>We are good in helping businesses grow in no time.</p>
  </div>
  <div class="footer-col" style="left:330px">
    <h5>Latest News</h5>
    <ul><li>Diam eu sapien et purus</li><li>Phasellus eget augue est</li><li>Usque ac gravida ligula</li><li>Proin ante arcu aliquam</li><li>Etiam in ullamcorper nisi</li><li>Mauris mollis magna</li></ul>
  </div>
  <div class="footer-col" style="left:620px">
    <h5>Useful Links</h5>
    <ul><li>Terms &amp; Conditions</li><li>Company Information</li><li>Documentation</li><li>Privacy Policy</li><li>Our Partners</li><li>Contact Us</li></ul>
  </div>
  <div class="footer-col contact" style="left:910px">
    <h5>Get In Touch</h5>
    <ul><li><span></span>12 Quayside Row<br>Leeds, UK</li><li><span></span>0113 555 0142</li><li><span></span>hello@harbourline.example</li><li><span></span>Live Chat</li></ul>
  </div>
</footer>

<div class="section copyright">© 2017 harbourline.example · All rights reserved</div>

</body>
</html>
```